Brenmoor Group needs a business card

I would like the card to be simple but modern and elegant.
I like black and white.
or black and gold.
we are a private finance lender and also are involved in property and property developments.

please look at the business card photos i provided i would like B.G only one one side and all the other details on the other side use fonts that tie in with my theme.

Industry/Entity Type

Finance

Contact Information for Business Card

Brenmoor Group (B.G) Callum Brenmoor M: 0418396152 E: callumbren@quivomail.com

Font styles to use
Other font styles liked:
• Use fonts that would reflect our business

Colors
000000
ffffff

Requirements
Must have
• one side of details
• other side has either B.G or Brenmoor Group like in the photos provided

```html
<!DOCTYPE html>
<html lang="en">
<head>
<meta charset="UTF-8">
<title>Brenmoor Group — Business Card</title>
<link rel="stylesheet" href="https://fonts.googleapis.com/css2?family=Open+Sans:wght@300;400&display=swap">
<style>
  :root {
    --ink: #000000;
    --paper: #ffffff;
    --frame: #111111;
    --shadow: rgba(0, 0, 0, 0.45);
    --rule: rgba(255, 255, 255, 0.9);
  }
  * { box-sizing: border-box; margin: 0; padding: 0; }
  html, body {
    width: 1200px;
    height: 1200px;
    overflow: hidden;
    background: var(--paper);
  }
  .canvas {
    position: relative;
    width: 1200px;
    height: 1200px;
    background: var(--paper);
    border: 3px solid var(--frame);
    font-family: "Open Sans", "Helvetica Neue", Arial, sans-serif;
  }
  .card {
    position: absolute;
    top: 239px;
    width: 415px;
    height: 726px;
    background: var(--ink);
    color: var(--paper);
    box-shadow: 14px 14px 12px -4px var(--shadow);
  }
  .card--details { left: 149px; }
  .card--brand { left: 635px; }

  .details {
    position: absolute;
    top: 310px;
    left: 0;
    width: 100%;
    text-align: center;
  }
  .details__name {
    font-size: 21px;
    font-weight: 400;
    letter-spacing: 1.5px;
    text-transform: uppercase;
    line-height: 1;
  }
  .rule {
    height: 1px;
    margin: 0 auto;
    background: linear-gradient(90deg, transparent 0%, var(--rule) 50%, transparent 100%);
  }
  .details .rule {
    width: 240px;
    margin-top: 19px;
    margin-bottom: 18px;
  }
  .details__contact {
    list-style: none;
    font-size: 16.5px;
    font-weight: 300;
    letter-spacing: 1.2px;
    line-height: 24px;
  }
  .details__label { margin-right: 8px; }

  .brand-name {
    position: absolute;
    top: 340px;
    left: 0;
    width: 100%;
    text-align: center;
    font-size: 34px;
    font-weight: 400;
    letter-spacing: 3px;
    text-transform: uppercase;
    line-height: 1;
  }
</style>
</head>
<body>
  <main class="canvas">
    <section class="card card--details" aria-label="Card front with contact details">
      <div class="details">
        <h1 class="details__name">Callum Brenmoor</h1>
        <div class="rule"></div>
        <ul class="details__contact">
          <li><span class="details__label">M:</span>041. 839. 6152</li>
          <li><span class="details__label">E:</span>callumbren@quivomail.com</li>
        </ul>
      </div>
    </section>

    <section class="card card--brand" aria-label="Card back with company name">
      <p class="brand-name">Brenmoor Group</p>
    </section>
  </main>
</body>
</html>
```